Recycling Depot Business Card Design

We need a double sided business card for our recycling depot business. Please include name, position, address, phone, cell, fax, email and website address. Business card should match the colour scheme of our logo and look environmental but modern. I've attached a few business cards from Mintvale Works that I like.

Industry/Entity Type

Recycling

Contact Information for Business Card

Please include name, position, address, phone, cell, fax, email and website address.

Font styles to use
Sans Serif

Requirements
Must have
• Our Logo, Colour Scheme that matches our logo. Use of Colour Gradients and a custom look.

```html
<!DOCTYPE html>
<html lang="en">
<head>
<meta charset="utf-8">
<title>Greenloop Resource Recovery – Business Card</title>
<link rel="stylesheet" href="https://fonts.googleapis.com/css2?family=Poppins:wght@400;500;700;800&display=swap">
<style>
  :root {
    --backdrop: #2b2b2b;
    --green-light: #a3cb38;
    --green-mid: #7dbb3f;
    --green-deep: #55ab47;
    --green-dark: #1e6b35;
    --green-title: #8dc63f;
    --ink: #1f1f1f;
    --paper: #ffffff;
  }
  * { box-sizing: border-box; margin: 0; padding: 0; }
  html, body {
    width: 1200px; height: 1189px; overflow: hidden;
    background: var(--backdrop);
    font-family: "Poppins", sans-serif;
  }
  .sheet {
    width: 1200px; height: 1189px;
    display: flex; flex-direction: column; align-items: center;
    gap: 60px; padding-top: 62px;
  }
  .card {
    width: 900px; height: 500px; border-radius: 28px;
    position: relative; overflow: hidden;
  }
  .card-front {
    background: linear-gradient(100deg, var(--green-light) 0%, var(--green-mid) 50%, var(--green-deep) 100%);
    display: flex; align-items: center; justify-content: center; gap: 34px;
  }
  .brand-dot {
    width: 120px; height: 120px; border-radius: 50%;
    background: var(--paper);
  }
  .brand-name {
    color: var(--paper); font-weight: 700; line-height: 1.05;
  }
  .brand-name .main { display: block; font-size: 92px; letter-spacing: -1px; }
  .brand-name .sub { display: block; font-size: 34px; padding-left: 6px; }

  .card-back {
    background: var(--paper);
    display: flex; align-items: center; justify-content: space-between;
    padding: 0 70px 0 80px;
  }
  .contact { display: flex; flex-direction: column; }
  .person-name {
    color: var(--green-dark); font-weight: 800; font-size: 34px;
    text-transform: uppercase; letter-spacing: 0.5px; line-height: 1.1;
  }
  .person-title {
    color: var(--green-title); font-weight: 500; font-size: 22px; margin-bottom: 36px;
  }
  .address { color: var(--ink); font-size: 20px; line-height: 1.3; margin-bottom: 24px; }
  .details { list-style: none; }
  .details li {
    display: flex; align-items: center; gap: 14px;
    color: var(--ink); font-size: 21px; line-height: 1.55;
  }
  .icon { width: 24px; height: 24px; flex: none; }
  .back-mark {
    display: flex; flex-direction: column; align-items: center; gap: 22px;
    margin-right: 20px;
  }
  .back-mark .brand-dot {
    width: 220px; height: 220px;
    background: linear-gradient(135deg, var(--green-title), var(--green-dark));
  }
  .back-mark .brand-label {
    color: var(--green-dark); font-weight: 700; font-size: 30px;
  }
</style>
</head>
<body>
<main class="sheet">
  <section class="card card-front" aria-label="Card front">
    <div class="brand-dot"></div>
    <p class="brand-name"><span class="main">Greenloop</span><span class="sub">Resource Recovery</span></p>
  </section>

  <section class="card card-back" aria-label="Card back">
    <div class="contact">
      <h1 class="person-name">Nora K. Ellis</h1>
      <p class="person-title">Executive Director</p>
      <p class="address">PO Box 418, 27 Alder Lane<br>Brookfield, USA</p>
      <ul class="details">
        <li>
          <svg class="icon" viewBox="0 0 24 24"><circle cx="12" cy="12" r="11" fill="#8dc63f"/><rect x="8" y="5" width="8" height="14" rx="1.5" fill="none" stroke="#fff" stroke-width="1.8"/></svg>
          555-201-4830
        </li>
        <li>
          <svg class="icon" viewBox="0 0 24 24"><circle cx="12" cy="12" r="11" fill="#8dc63f"/><rect x="6" y="10" width="12" height="7" rx="1" fill="#fff"/><rect x="8.5" y="6" width="7" height="4" fill="none" stroke="#fff" stroke-width="1.5"/></svg>
          555-201-4831
        </li>
        <li>
          <svg class="icon" viewBox="0 0 24 24"><circle cx="12" cy="12" r="11" fill="#8dc63f"/><path d="M8 6c-1 1-1 3 0 5l3 4c2 2 4 3 5 2l1-1-2.5-2.5-1.5 1-3-3.5 1-1.5L8.5 6z" fill="#fff"/></svg>
          555-201-4832
        </li>
        <li>
          <svg class="icon" viewBox="0 0 24 24"><circle cx="12" cy="12" r="11" fill="#8dc63f"/><rect x="6" y="8" width="12" height="8" fill="none" stroke="#fff" stroke-width="1.6"/><path d="M6 8l6 5 6-5" fill="none" stroke="#fff" stroke-width="1.6"/></svg>
          info@greenloopmail.com
        </li>
        <li>
          <svg class="icon" viewBox="0 0 24 24"><circle cx="12" cy="12" r="11" fill="#8dc63f"/><circle cx="12" cy="12" r="6" fill="none" stroke="#fff" stroke-width="1.5"/><path d="M6 12h12M12 6c-3 3-3 9 0 12M12 6c3 3 3 9 0 12" fill="none" stroke="#fff" stroke-width="1.2"/></svg>
          www.greenloopdepot.com
        </li>
      </ul>
    </div>
    <div class="back-mark">
      <div class="brand-dot"></div>
      <p class="brand-label">Greenloop</p>
    </div>
  </section>
</main>
</body>
</html>
```